BUSINESS CARD FOR GUITAR SCHOOL

I would like to design a business card for my Guitar Music School. The school is called "Pluck & Lantern".

The card should be yellow.

Target Market(s)

18-35 years old

Industry/Entity Type

School

Contact Information for Business Card

I would like to design a business card for my Guitar Music School. The school is called "Pluck & Lantern". The card should be yellow.

Card must be consistent with my website design: www.pluckandlantern.com.sg

Requirements
Must have
• 1) Name of Company
• 2) Company Logo
• 3) Name of Employee
• 4) Position of Employee
• 5) Contact Number
• 6) Address
Nice to have
• Creative Design
• Card must be consistent with my website design: www.pluckandlantern.com.sg
Should not have
• Boring Design

```html
<!DOCTYPE html>
<html lang="en">
<head>
<meta charset="utf-8">
<title>Pluck &amp; Lantern — Business Card</title>
<link rel="stylesheet" href="https://fonts.googleapis.com/css2?family=Dosis:wght@400;500;800&display=swap">
<style>
  :root {
    --bg: #e6e6e6;
    --yellow: #e8b124;
    --ink: #262626;
    --paper: #f2f2f2;
    --card-w: 900px;
    --card-h: 514px;
  }
  * { box-sizing: border-box; margin: 0; padding: 0; }
  html, body { width: 1200px; height: 1200px; overflow: hidden; }
  body {
    background: var(--bg);
    font-family: "Dosis", sans-serif;
    color: var(--ink);
    display: flex;
    flex-direction: column;
    align-items: center;
    justify-content: center;
    gap: 56px;
  }
  .card {
    width: var(--card-w);
    height: var(--card-h);
    position: relative;
    overflow: hidden;
    box-shadow: 0 6px 18px rgba(0,0,0,0.12);
  }

  /* Brand lockup */
  .brand {
    display: flex;
    flex-direction: column;
    align-items: flex-start;
    white-space: nowrap;
  }
  .brand-row {
    display: flex;
    align-items: center;
    gap: 16px;
  }
  .brand-dot {
    width: 34px;
    height: 34px;
    border-radius: 50%;
    background: var(--ink);
    flex: none;
  }
  .brand-name {
    font-weight: 800;
    font-size: 70px;
    line-height: 1;
    letter-spacing: -1px;
    color: var(--ink);
    white-space: nowrap;
  }
  .brand-tagline {
    font-weight: 500;
    font-size: 18px;
    margin-top: 8px;
    margin-left: 50px;
    color: var(--ink);
  }

  /* Front */
  .card-front { background: var(--yellow); }
  .card-front .brand {
    position: absolute;
    left: 50%;
    top: 180px;
    transform: translateX(-50%);
  }
  .front-rule {
    position: absolute;
    left: 0;
    right: 0;
    top: 398px;
    height: 3px;
    background: var(--ink);
  }
  .front-web {
    position: absolute;
    left: 0;
    right: 0;
    top: 430px;
    text-align: center;
    font-size: 28px;
    font-weight: 500;
    letter-spacing: 0.5px;
  }

  /* Back */
  .card-back { background: var(--paper); }
  .back-edge {
    position: absolute;
    left: 0; right: 0; bottom: 0;
    height: 12px;
    background: var(--yellow);
  }
  .card-back .brand {
    position: absolute;
    left: 56px;
    top: 225px;
  }
  .card-back .brand-name { font-size: 52px; }
  .card-back .brand-dot { width: 26px; height: 26px; }
  .card-back .brand-row { gap: 14px; }
  .card-back .brand-tagline { font-size: 15px; margin-left: 40px; }
  .back-company {
    position: absolute;
    left: 520px;
    top: 40px;
    font-size: 34px;
    font-weight: 500;
  }
  .contact-panel {
    position: absolute;
    left: 500px;
    right: 0;
    top: 100px;
    height: 300px;
    background: var(--yellow);
    padding: 34px 30px 0 34px;
    font-size: 25px;
    line-height: 1.22;
  }
  .employee-name { font-weight: 500; font-size: 26px; }
  .employee-role { font-size: 20px; margin-left: 100px; margin-bottom: 16px; }
</style>
</head>
<body>

  <section class="card card-front" aria-label="Card front">
    <div class="brand">
      <div class="brand-row">
        <span class="brand-dot"></span>
        <span class="brand-name">Pluck &amp; Lantern</span>
      </div>
      <span class="brand-tagline">Tuning Hearts One Chord at a Time</span>
    </div>
    <div class="front-rule"></div>
    <p class="front-web">www.pluckandlantern.com.sg</p>
  </section>

  <section class="card card-back" aria-label="Card back">
    <div class="brand">
      <div class="brand-row">
        <span class="brand-dot"></span>
        <span class="brand-name">Pluck &amp; Lantern</span>
      </div>
      <span class="brand-tagline">Tuning Hearts One Chord at a Time</span>
    </div>
    <h2 class="back-company">Pluck &amp; Lantern</h2>
    <div class="contact-panel">
      <p class="employee-name">Employee&nbsp;&nbsp;Name</p>
      <p class="employee-role">Position</p>
      <p>+65 9100 4821</p>
      <p>27 Kestrel Lane</p>
      <p>Harbour Block B #05-12</p>
      <p>Singapore 408812</p>
      <p>www.pluckandlantern.com.sg</p>
    </div>
    <div class="back-edge"></div>
  </section>

</body>
</html>
```